Business Card Design Project

We need a business card design for a management consultancy focused on financial innovation and digital money, run by experts from the Financial Services, Telecoms and Money Transfer industries.
Our products include services such as Mobile Payments, Mobile Money, Digital Wallets, Online Payments, Branchless Banking and more. We work with regulatory information, business plans, financial modelling, strategic planning, new products functional specification, new technologies evaluation, etc.
See company logo attached.
We would like to see 2 versions: one in portuguese and one in english (regarding data information). You can see below information needed (whenever there is a difference between the two versions, the first one is in english and the second one in portuguese).

Name
Position
Phone/ Tel: ++61-3-xxxx-xxxx
Cell/ Cel: ++61-3-4 xxxx-xxxx
Dr. Tavares Lobato Av., 318 - Block C - 9th level / Avenida Dr. Tavares Lobato, 318 - Torre II - 16o. andar
São Paulo - SP
01327-118 - Brazil/ 01327-118 - Brasil

Target Market(s)

Audience: C-level executives from banks, credit card companies, acquirers, IT developers, retailers

Industry/Entity Type

Financial

Requirements
Must have
• Must use the logo and information above. Front must have white background. Back side should have only logo.
Nice to have
• Back should be in another colour but if it seems too exxagerated, maintain back in white also.
Should not have
• Do not add other illustrations to the business card.

```html
<!DOCTYPE html>
<html lang="en">
<head>
<meta charset="utf-8">
<title>T Arkwright Management Consulting – Business Card</title>
<link rel="stylesheet" href="https://fonts.googleapis.com/css2?family=Tinos:wght@400;700&display=swap">
<style>
  :root {
    --stage: #ecebe8;
    --card-white: #ffffff;
    --card-grey: #9a9a9a;
    --navy: #1f2f6b;
    --ink: #2b2b2b;
    --muted: #444444;
    --faint: #e4e6ea;
    --shadow: rgba(0, 0, 0, 0.18);
  }
  * { margin: 0; padding: 0; box-sizing: border-box; }
  html, body {
    width: 1200px;
    height: 784px;
    overflow: hidden;
    background: var(--stage);
    font-family: "Tinos", "Times New Roman", serif;
  }
  .stage {
    position: relative;
    width: 1200px;
    height: 784px;
  }
  .card {
    position: absolute;
    top: 237px;
    width: 540px;
    height: 310px;
    border-radius: 3px;
    box-shadow: 0 6px 18px var(--shadow);
    overflow: hidden;
  }
  .card--back {
    left: 40px;
    background: var(--card-grey);
    display: flex;
    align-items: center;
    justify-content: center;
  }
  .card--front {
    left: 620px;
    background: var(--card-white);
  }
  .brand {
    display: flex;
    align-items: center;
    gap: 12px;
    color: var(--navy);
    font-weight: 400;
  }
  .brand__mark {
    width: 38px;
    height: 38px;
    background: var(--navy);
    flex: none;
  }
  .brand__name {
    display: flex;
    flex-direction: column;
    line-height: 1;
    text-transform: uppercase;
  }
  .brand__title { font-size: 30px; letter-spacing: 1px; }
  .brand__sub { font-size: 13.5px; letter-spacing: 1.2px; margin-top: 4px; }
  .card--front .brand {
    position: absolute;
    left: 48px;
    top: 58px;
  }
  .decor-block {
    position: absolute;
    right: -30px;
    bottom: -40px;
    width: 170px;
    height: 170px;
    background: var(--faint);
  }
  .holder {
    position: absolute;
    left: 88px;
    top: 150px;
  }
  .holder__name {
    color: var(--navy);
    font-size: 19px;
  }
  .holder__role {
    color: var(--ink);
    font-size: 11.5px;
    margin-top: 7px;
  }
  .contact {
    position: absolute;
    left: 88px;
    top: 208px;
    list-style: none;
    font-size: 12.5px;
    color: var(--muted);
  }
  .contact__item {
    display: flex;
    align-items: center;
    gap: 7px;
    height: 17px;
    white-space: nowrap;
  }
  .contact__icon {
    width: 12px;
    height: 12px;
    fill: var(--navy);
    flex: none;
  }
  .contact__item--continued { padding-left: 19px; }
</style>
</head>
<body>
<main class="stage">
  <section class="card card--back" aria-label="Card back">
    <div class="brand">
      <span class="brand__mark"></span>
      <span class="brand__name">
        <span class="brand__title">T Arkwright</span>
        <span class="brand__sub">Management Consulting</span>
      </span>
    </div>
  </section>

  <section class="card card--front" aria-label="Card front">
    <div class="decor-block"></div>
    <div class="brand">
      <span class="brand__mark"></span>
      <span class="brand__name">
        <span class="brand__title">T Arkwright</span>
        <span class="brand__sub">Management Consulting</span>
      </span>
    </div>

    <div class="holder">
      <p class="holder__name">Dr. Tavares Lobato</p>
      <p class="holder__role">Founder and Managing Partner</p>
    </div>

    <ul class="contact">
      <li class="contact__item">
        <svg class="contact__icon" viewBox="0 0 24 24"><path d="M6.6 10.8a15.2 15.2 0 0 0 6.6 6.6l2.2-2.2c.3-.3.7-.4 1-.2 1.1.4 2.3.6 3.6.6.6 0 1 .4 1 1V20c0 .6-.4 1-1 1A17 17 0 0 1 3 4c0-.6.4-1 1-1h3.5c.6 0 1 .4 1 1 0 1.3.2 2.5.6 3.6.1.3 0 .7-.2 1z"/></svg>
        <span>++61-3-xxxx-xxxx</span>
      </li>
      <li class="contact__item">
        <svg class="contact__icon" viewBox="0 0 24 24"><path d="M7 1h10a2 2 0 0 1 2 2v18a2 2 0 0 1-2 2H7a2 2 0 0 1-2-2V3a2 2 0 0 1 2-2zm0 4v13h10V5zm5 14.5a1 1 0 1 0 0 2 1 1 0 0 0 0-2z"/></svg>
        <span>++61-3-4 xxxx-xxxx</span>
      </li>
      <li class="contact__item">
        <svg class="contact__icon" viewBox="0 0 24 24"><path d="M2 5h20v14H2zm2 2v.5l8 5 8-5V7zm0 2.8V17h16V9.8l-8 5z"/></svg>
        <span>email@tarkwright.com</span>
      </li>
      <li class="contact__item">
        <svg class="contact__icon" viewBox="0 0 24 24"><path d="M12 3l10 9h-3v9h-5v-6h-4v6H5v-9H2z"/></svg>
        <span>Av., 318 - Block C - 9th level</span>
      </li>
      <li class="contact__item contact__item--continued">
        <span>/ Avenida Dr. Tavares Lobato,</span>
      </li>
    </ul>
  </section>
</main>
</body>
</html>
```